"Lanterns Along Every Quiet Road" Sermon Series Design

Needing a design for our church's next sermon series titled "Lanterns Along Every Quiet Road" where we will discuss the need for unity, diversity, love and clarity. Looking for a 1920 x 1080 (or higher res) editable and layered file (PSD or AI) so that we can reformat the design to work on social, screens, lower thirds and various print and online mediums. We will also need to have access to the font files so that we can make resize and tweak as needed. We like the idea of using a globe or map of the world as the backdrop with the words overtop. Or, the idea of creating a bunch of newspaper clippings (generic, so that they can't actually be read) and making the shape of a heart. See attached examples. This website will give you an idea of our previous sermon series designs so you can have an idea of our style (but, feel free to help us advance the ball on something more aligned with current design trends): https://www.brambleford.example/series

Examples use red, but stay away from a ton of red. If you're gonna major in a color, use blue or something in that family.

Must haves:
Title: Lanterns Along Every Quiet Road
Tagline : (TBD - use some Lorem Ipsum as a placeholder and we will fill in later)
Our Logo (attached) (small towards bottom is standard - only use solid colors for logo - preferably just solid black or white)

Industry/Entity Type

Church

Font styles to use
Serif
Sans Serif

Requirements
Must have
• Title: Lanterns Along Every Quiet Road
Nice to have
• We like the idea of using a globe or map of the world as the backdrop with the words overtop. Or, the idea of creating a bunch of newspaper clippings (generic, so that they can't actually be read) and making the shape of a heart. See attached examples.

If you're gonna major on a color, stick with blue or something close.
Should not have
• Don't use red as the primary color (example we sent has red, but stay away from it)

```html
<!DOCTYPE html>
<html lang="en">
<head>
<meta charset="utf-8">
<title>Lanterns Along Every Quiet Road — Sermon Series</title>
<link rel="stylesheet" href="https://fonts.googleapis.com/css2?family=Jost:wght@300;400&family=Source+Sans+3:wght@400&display=swap">
<style>
  :root {
    --page: #ffffff;
    --ink: #050608;
    --sky-core: #00abe8;
    --sky-mid: #2f8cc8;
    --sky-edge: #4a6ba1;
    --sky-corner: #41618a;
    --frame-line: #3b5577;
    --globe-land: #1f3a47;
    --globe-sea: #0ea4dd;
  }
  * { margin: 0; padding: 0; box-sizing: border-box; }
  html, body {
    width: 1200px; height: 796px; overflow: hidden;
    background: var(--page);
  }
  .canvas { position: relative; width: 1200px; height: 796px; background: var(--page); }
  .series-card {
    position: absolute; left: 138px; top: 138px; width: 920px; height: 518px;
    border: 1px solid var(--frame-line);
    background: radial-gradient(ellipse 70% 78% at 50% 44%,
      var(--sky-core) 0%, var(--sky-mid) 38%, var(--sky-edge) 68%, var(--sky-corner) 100%);
    color: var(--ink);
    font-family: "Jost", "Futura", sans-serif;
  }
  .title-kicker, .title-closer {
    position: absolute; left: 0; right: 0; text-align: center;
    font-weight: 400; font-size: 40px; line-height: 1;
    letter-spacing: 0.28em; text-indent: 0.28em; text-transform: uppercase;
  }
  .title-kicker { top: 133px; font-size: 34px; }
  .title-closer { top: 291px; }
  .title-hero {
    position: absolute; left: 0; right: 0; top: 180px; height: 112px;
    display: flex; justify-content: center; align-items: center;
    font-weight: 300; font-size: 136px; line-height: 1;
    letter-spacing: 0.02em; text-transform: uppercase;
  }
  .globe-letter { width: 118px; height: 118px; margin-right: 6px; flex: none; }
  .tagline {
    position: absolute; left: 0; right: 0; top: 380px; text-align: center;
    font-family: "Source Sans 3", "Myriad Pro", sans-serif;
    font-size: 17px; letter-spacing: 0.01em;
  }
  .church-mark {
    position: absolute; left: 0; right: 0; top: 452px;
    display: flex; justify-content: center; align-items: center; gap: 9px;
    font-size: 17px; font-weight: 400; letter-spacing: 0.04em;
  }
  .church-mark-dot {
    width: 18px; height: 18px; border-radius: 50%; border: 2px solid var(--ink);
  }
</style>
</head>
<body>
<main class="canvas">
  <section class="series-card">
    <h1>
      <span class="title-kicker">Lanterns Along Every</span>
      <span class="title-hero">
        <svg class="globe-letter" viewBox="0 0 118 118" role="img" aria-label="Globe showing Europe and Africa, forming the letter Q">
          <defs>
            <radialGradient id="globeFill" cx="45%" cy="35%" r="65%">
              <stop offset="0" stop-color="var(--globe-land)"/>
              <stop offset="0.55" stop-color="#1b5f7e"/>
              <stop offset="1" stop-color="var(--globe-sea)"/>
            </radialGradient>
          </defs>
          <circle cx="56" cy="56" r="54" fill="url(#globeFill)"/>
          <line x1="84" y1="88" x2="112" y2="114" stroke="var(--ink)" stroke-width="5" stroke-linecap="square"/>
        </svg>
        <span class="hero-rest">uiet</span>
      </span>
      <span class="title-closer">Road</span>
    </h1>
    <p class="tagline">Lorem ipsum dolor sit amet, consectetuer adipiscing elit</p>
    <div class="church-mark">
      <span class="church-mark-dot"></span>
      <span class="church-mark-name">Brambleford Church</span>
    </div>
  </section>
</main>
</body>
</html>
```